Agricultural Consulting Website

Provide a modern yet business like website for my new Agriculture Consulting Business in Australia called FenTrove. Whilst we are based in Australia we are targetting both domestic and international markets (especially in Asia). We are targetting corporate, small business, government and farmer clients. The design should compliment our logo also sourced through pixel guild. The webiste should be easy for me to keep updated on a regular basis without the need to go back to the designer.

Industry/Entity Type

Business

Requirements
Must have
• clean crisp feel
• be modern yet business like
• be able to be updated by myself easily

```html
<!DOCTYPE html>
<html lang="en">
<head>
<meta charset="utf-8">
<title>FenTrove — Agricultural Consulting</title>
<link href="https://fonts.googleapis.com/css2?family=Ubuntu:wght@400;500&family=Open+Sans:ital,wght@0,400;0,600;1,400&display=swap" rel="stylesheet">
<style>
:root{
  --bg:#231507;
  --white:#ffffff;
  --green:#669900;
  --green-light:#7cb800;
  --brown:#5b2b00;
  --brown-btn:#6b2d05;
  --text:#3a3a3a;
  --rule:#dddddd;
  --panel:#f4f4f4;
}
*{margin:0;padding:0;box-sizing:border-box}
html,body{width:875px;height:1200px;overflow:hidden;background:var(--bg)}
body{position:relative;font-family:"Open Sans",sans-serif;color:var(--text);font-size:8.6px;line-height:1.55}
.abs{position:absolute}
.topbar-phone{left:108px;top:8px;color:#fff;font-size:10.5px;display:flex;align-items:center;gap:6px}
.topbar-search{right:100px;top:10px;color:#fff;font-size:8.5px;letter-spacing:.3px;display:flex;align-items:center;gap:10px}
.search-btn{width:16px;height:16px;border-radius:50%;background:#3a2a18;display:flex;align-items:center;justify-content:center}
.page{left:83px;top:31px;width:711px;height:879px;background:var(--white)}
.logo{left:29px;top:19px;display:flex;align-items:center;gap:6px;font-family:"Ubuntu",sans-serif;font-size:24px;color:var(--green)}
.logo-mark{width:30px;height:30px;background:var(--brown)}
.nav{left:352px;top:21px;width:363px;height:37px;background:var(--green);display:flex;padding:7px 0 0 19px;gap:0}
.nav a{color:#fff;text-decoration:none;font-size:9px;line-height:1.2;display:block}
.nav a small{display:block;font-size:6.5px;opacity:.9}
.nav .i1{width:66px}.nav .i2{width:60px}.nav .i3{width:79px}.nav .i4{width:63px}
.hero{left:0;top:79px;width:711px;height:246px;background:linear-gradient(180deg,#b9d2e8 0%,#e7e0c2 22%,#a58a3a 33%,#6f8a2a 40%,#4f8a1c 60%,#2f6a10 100%)}
.hero-caption{left:11px;top:68px;width:238px;height:114px;background:rgba(40,50,20,.55);padding:8px 21px;color:#fff}
.hero-caption h2{font-family:"Ubuntu",sans-serif;font-weight:400;font-size:13.5px;margin-bottom:9px}
.hero-caption p{font-size:8.2px;font-weight:600;line-height:1.5}
.btn-read{display:inline-block;margin-top:10px;background:var(--brown-btn);color:#fff;font-size:8.5px;padding:5px 17px}
.dots{right:28px;top:229px;display:flex;gap:2px}
.dots i{width:5px;height:5px;background:#fff}.dots i:first-child{background:var(--green-light)}
.feature{top:358px;width:145px}
.feature h3{font-family:"Ubuntu",sans-serif;font-weight:500;font-size:13px;color:var(--brown);margin-top:12px;height:38px}
.feature p{font-size:7.8px;line-height:1.62}
.feature .more{color:var(--green-light);float:right}
.ficon{position:absolute;right:0;top:0;width:38px;height:40px;border:1.5px solid var(--green);display:flex;align-items:center;justify-content:center}
.welcome-photo{left:22px;top:471px;width:168px;height:148px;border-radius:50%;border:4px solid var(--green);background:radial-gradient(circle at 50% 40%,#9a8a6a,#5d6b35 60%,#3f5a1c)}
.welcome h2{font-family:"Ubuntu",sans-serif;font-weight:400;font-size:19px;color:var(--brown)}
.welcome h2 span{color:var(--green)}
.welcome{left:211px;top:480px;width:480px}
.welcome p{margin-top:12px;font-size:8.2px;line-height:1.75;padding-left:3px}
.sec-title{font-family:"Ubuntu",sans-serif;font-size:13.5px;color:var(--brown)}
.news{left:19px;top:636px;width:323px}
.pager{position:absolute;right:0;top:4px;display:flex;gap:1px}
.pager i{width:16px;height:14px;background:#cfcfcf;color:#fff;font-style:normal;font-size:9px;text-align:center;transform:skewX(-10deg)}
.news-item h4{font-size:8.6px;font-weight:600;margin-top:18px;padding:0 0 4px 11px;border-bottom:1px solid var(--rule);position:relative}
.news-item h4:before{content:"›";position:absolute;left:0;top:-1px;color:#999}
.news-item p{padding:6px 2px;border-bottom:1px solid var(--rule);font-size:8.3px;line-height:1.6}
.news-item em{display:block;color:var(--green-light);font-size:7.8px;margin-top:5px}
.why{left:371px;top:636px;width:322px}
.acc{margin-top:13px;border:1px solid var(--rule)}
.acc-h{background:var(--panel);font-weight:600;font-size:8.3px;padding:3px 8px 3px 19px;position:relative;border-top:1px solid #fff}
.acc-h:before{content:"+";position:absolute;left:7px;color:#888}
.acc-h.open{color:var(--green-light)}.acc-h.open:before{content:"–"}
.acc-b{padding:5px 7px;font-size:8.3px;line-height:1.6;border-bottom:1px solid var(--rule)}
.acc-h+.acc-h,.acc-b+.acc-h{border-top:3px solid #fff}
.footer{left:83px;top:920px;width:711px;height:240px;background:var(--white)}
.fcol{top:13px}
.fcol h3{font-family:"Ubuntu",sans-serif;font-weight:400;font-size:13.5px;color:var(--brown);margin-bottom:10px}
.fcol p{font-size:8.2px;line-height:1.6;margin-bottom:17px;padding-left:2px}
.fcol p a{color:var(--green-light)}
.field{width:164px;height:20px;border:1px solid #ddd;margin-bottom:4px;padding:4px 6px;font-size:8.4px}
.field.msg{height:77px}
.btn-send{display:inline-block;background:var(--green-light);color:#fff;font-size:8.5px;padding:2px 13px;border-radius:3px;margin-top:3px}
.testi{font-family:Arial,sans-serif;width:168px}
.testi h3{margin-bottom:8px}
.testi p.q{font-size:8.2px;line-height:11.6px;margin-bottom:0;padding-left:0;text-indent:23px;position:relative}
.testi .bubble{position:absolute;left:0;top:2px;width:11px;height:8px;border-radius:50%;background:var(--green-light)}
.testi .who{color:var(--green-light);font-size:8.2px;line-height:11px;margin:6px 0 8px}
.testi hr{border:0;border-top:1px solid var(--rule);margin-bottom:10px}
.social li{list-style:none;display:flex;align-items:center;gap:20px;height:29px;font-size:8.6px}
.social .sq{width:13px;height:13px;border-radius:2px}
.copy{left:102px;top:1173px;color:#fff;font-size:8.4px}
.legal{right:100px;top:1173px;color:#fff;font-size:8.4px;display:flex;gap:20px}
</style>
</head>
<body>
<div class="abs topbar-phone">
  <svg width="10" height="11" viewBox="0 0 10 11"><path d="M2 0.5 L3.6 2.8 L2.6 4 Q3.6 6.6 6 8 L7.2 7 L9.5 8.6 L8.3 10.5 Q2.5 9.5 0.5 2 Z" fill="#fff"/></svg>
  <span>0800-555-0190</span>
</div>
<div class="abs topbar-search">SEARCH THE SITE
  <span class="search-btn"><svg width="8" height="8" viewBox="0 0 8 8"><circle cx="3.2" cy="3.2" r="2.3" fill="none" stroke="#aaa" stroke-width="1.2"/><path d="M5 5 L7.5 7.5" stroke="#aaa" stroke-width="1.4"/></svg></span>
</div>

<div class="abs page">
  <div class="abs logo"><span class="logo-mark"></span>FenTrove</div>
  <nav class="abs nav">
    <a class="i1" href="#">HOME<small>Welcome</small></a>
    <a class="i2" href="#">BLOG<small>Our blog</small></a>
    <a class="i3" href="#">PORTFOLIO<small>Our projects</small></a>
    <a class="i4" href="#">ABOUT<small>We are best</small></a>
    <a href="#">CONTACT<small>Get in touch</small></a>
  </nav>

  <div class="abs hero" role="img" aria-label="Rows of green crops stretching to rolling golden hills under a blue sky">
    <div class="abs hero-caption">
      <h2>Quality Of Agriculture In Asia</h2>
      <p>Lorem Ipsum est simplement du faux texte employé dans la sition et la misen page avant impression...</p>
      <span class="btn-read">READ MORE</span>
    </div>
    <div class="abs dots"><i></i><i></i><i></i><i></i></div>
  </div>

  <div class="abs feature" style="left:23px"><div class="ficon"><svg width="18" height="22" viewBox="0 0 18 22"><circle cx="9" cy="5" r="3" fill="var(--brown)"/><rect x="6" y="9" width="6" height="12" fill="var(--brown)"/></svg></div><h3>Farming</h3><p>Lorem Ipsum est simplement du faux texte mployé dans la sition et la misen page avant impression... <span class="more">More&gt;&gt;</span></p></div>
  <div class="abs feature" style="left:198px"><div class="ficon"><svg width="18" height="22" viewBox="0 0 18 22"><path d="M4 20 L14 4" stroke="var(--brown)" stroke-width="2"/><ellipse cx="12" cy="9" rx="2.5" ry="5" fill="var(--brown)" transform="rotate(30 12 9)"/></svg></div><h3>Croping</h3><p>Lorem Ipsum est simplement du faux texte mployé dans la sition et la misen page avant impression... <span class="more">More&gt;&gt;</span></p></div>
  <div class="abs feature" style="left:370px"><div class="ficon"><svg width="24" height="18" viewBox="0 0 24 18"><rect x="3" y="4" width="14" height="7" fill="var(--brown)"/><circle cx="6" cy="13" r="3.5" fill="var(--brown)"/><circle cx="17" cy="14" r="2.5" fill="var(--brown)"/></svg></div><h3>Fertilization</h3><p>Lorem Ipsum est simplement du faux texte mployé dans la sition et la misen page avant impression... <span class="more">More&gt;&gt;</span></p></div>
  <div class="abs feature" style="left:543px"><div class="ficon"><svg width="20" height="22" viewBox="0 0 20 22"><path d="M10 21 V6" stroke="var(--brown)" stroke-width="2"/><path d="M10 12 Q3 12 3 6 Q9 6 10 12 M10 12 Q17 12 17 6 Q11 6 10 12" fill="var(--brown)"/></svg></div><h3>Better Growth</h3><p>Lorem Ipsum est simplement du faux texte mployé dans la sition et la misen page avant impression... <span class="more">More&gt;&gt;</span></p></div>

  <div class="abs welcome-photo" role="img" aria-label="Smiling farmer tending young plants in a field"></div>
  <div class="abs welcome">
    <h2>Welcome to the <span>FenTrove Agriculture Australia</span></h2>
    <p>Lorem Ipsum est simplement du faux texte employé dans la sition et la misen page avant impression. Le Lorem Ipsum est le faux texte standard de l'imprimerie depuis les années 1500, quand un peintre anonyme assembla ensemble des morceaux de texte pour réaliser un livre spécimen de polices de texte. Il n'a pas fait que survivre cinq siècles, mais s'est aussi adapté à la bureautique informatique, sans que son contenu n'en soit modifié. Il a été popularisé dans les années 1960, Lorem Ipsum est simplement du faux texte employé dans la sition et la misen page avant impression. Le Lorem Ipsum est le faux texte standard de l'imprimerie depuis les années 1500.</p>
  </div>

  <div class="abs news">
    <div class="sec-title">Agricultural News</div>
    <div class="pager"><i>–</i><i>+</i></div>
    <div class="news-item"><h4>Ut enim ad minim veniam</h4><p>Lorem Ipsum est simplement du faux texte employé dans la sition et la misen page avant impression. Le Lorem Ipsum est le faux texte standard de l'imprimerie depuis les années 1500, quand un peintre anonyme assembla</p><em>Posted by Merrin On June 3, 2013</em></div>
    <div class="news-item" style="margin-top:10px"><h4>Vestibulum ante ipsum primis in faucibus</h4><p>Lorem Ipsum est simplement du faux texte employé dans la sition et la misen page avant impression. Le Lorem Ipsum est le faux texte standard de l'imprimerie depuis les années 1500, quand un peintre anonyme assembla</p><em>Posted by Merrin On June 3, 2013</em></div>
  </div>

  <div class="abs why">
    <div class="sec-title">Why Choose US ?</div>
    <div class="acc">
      <div class="acc-h open">Lorem Ipsum est simplement du faux</div>
      <div class="acc-b">Lorem Ipsum est simplement du faux texte employé dans la sition et la misen page avant impression. Le Lorem Ipsum est le faux texte standard de l'imprimerie depuis les années 1500, quand un peintre anonyme</div>
      <div class="acc-h">Simplement du faux texte employé dans la sition et la misen</div>
      <div class="acc-h">Lorem Ipsum est simplement du faux</div>
      <div class="acc-h">Simplement du faux texte employé dans la sition et la misen</div>
    </div>
  </div>
</div>

<footer class="abs footer">
  <div class="abs fcol" style="left:19px;width:150px">
    <h3>What We Do ?</h3>
    <p>Lorem Ipsum est simplement du faux texte mployé dans la sition et la misen page <a>avant impression...</a></p>
    <p>Lorem Ipsum est simplement du faux texte mployé dans la sition et la misen page <a>avant impression...</a></p>
    <p>Lorem Ipsum est simplement du faux texte mployé dans la sition et la misen page <a>avant impression...</a></p>
  </div>
  <div class="abs fcol" style="left:195px">
    <h3>Get In Touch</h3>
    <div class="field">Name</div>
    <div class="field">Email</div>
    <div class="field msg">Message</div>
    <span class="btn-send">Send</span>
  </div>
  <div class="abs fcol testi" style="left:375px">
    <h3>Testimonial</h3>
    <p class="q"><span class="bubble"></span>Orci nisi, luctus vitae imperdiet a, iquam vel urna. Pellentesque tincidunt laoreet est, in tristique sapien consequat a purus at ullamcorper pulvinar, massa libero magna.</p>
    <div class="who">Tessa Lund, Company inc.</div>
    <hr>
    <p class="q"><span class="bubble"></span>Luctus vitae imperdiet a, iquamorci nisi lorem. Pellentesque tincidunt laoreet est, in tristique sapien consequat a purus at ullam pulvinar, massa libero consequat egestas mas.</p>
    <div class="who">Owen Pike, Company inc.</div>
  </div>
  <div class="abs fcol" style="left:576px">
    <h3>Social Media</h3>
    <ul class="social">
      <li><span class="sq" style="background:#3b5998"></span>Friendwall</li>
      <li><span class="sq" style="background:#29a9e0"></span>Chirper</li>
      <li><span class="sq" style="background:#1b6fa8"></span>Workline</li>
      <li><span class="sq" style="background:#e04a32"></span>Circleup</li>
      <li><span class="sq" style="background:#20a4e0"></span>Callway</li>
    </ul>
  </div>
</footer>

<div class="abs copy">Copyright © 2013 FenTrove Agriculture ltd All Rights Reserved</div>
<div class="abs legal"><span>Terms &amp; Condition</span><span>|</span><span>Privacy Policy</span></div>
</body>
</html>
```